Business card design for new eCommerce site focusing on integrity and strong businsess tactics

We need a business card that will stand out and be memorable. Something with color that matches our company logo colors. Think high end version of Dealvine. There are 2 logos provided. The parent company is called Bright Harbor Ventures and we are presenting a new and very exciting eCommerce site called KeenTraders.example.

Target Market(s)

Our target markets are in the Activities, Food and Beverage, Health and Beauty

Industry/Entity Type

Marketing

Contact Information for Business Card

We have 4 members that need cards...I will provide all info to the winner of the design contest
Business Address is
48730 West 61st Avenue, Suite C204
Phoenix AZ 85917

Font styles to use
Serif
Sans Serif

Colors

Designer to choose colors to be used in the design.

Requirements
Must have
• The card must be memorable...should be unique in design but must exude integrity and be playful .
• I have provided several colors or our parent company...please feel free to use which ever
Nice to have
• I will leave this up to you. Feel free to use other images of your choosing that wraps around our client.....Activities, Dining, Health, Beauty
Should not have
• just dont be boring

```html
<!DOCTYPE html>
<html lang="en">
<head>
<meta charset="utf-8">
<title>KeenTraders.example — Business Card</title>
<link href="https://fonts.googleapis.com/css2?family=Jost:wght@400;500;600&display=swap" rel="stylesheet">
<style>
  :root {
    --backdrop: #2a2a2a;
    --card-white: #f4f4f4;
    --leaf-green: #7dc242;
    --lime: #a8cf45;
    --ocean-blue: #2c7fb2;
    --sky-cyan: #3fbcd6;
    --text-grey: #4a4a4a;
    --white: #ffffff;
  }
  * { margin: 0; padding: 0; box-sizing: border-box; }
  html, body { width: 1200px; height: 960px; overflow: hidden; }
  body {
    background: var(--backdrop);
    font-family: "Jost", sans-serif;
    position: relative;
  }
  .card {
    position: absolute;
    width: 600px;
    height: 343px;
    border-radius: 22px;
    overflow: hidden;
  }
  .card-front { left: 302px; top: 130px; background: var(--card-white); }
  .card-back {
    left: 299px; top: 490px; height: 342px;
    background: linear-gradient(135deg, var(--sky-cyan) 0%, var(--ocean-blue) 38%, var(--ocean-blue) 100%);
  }

  /* front: brand block */
  .brand {
    position: absolute; left: 95px; top: 72px;
    display: flex; align-items: center; gap: 18px;
  }
  .brand-dot {
    width: 62px; height: 62px; border-radius: 50%;
    background: var(--leaf-green);
  }
  .brand-name {
    font-size: 35px; font-weight: 500; color: var(--ocean-blue);
    line-height: 1; letter-spacing: -0.5px;
  }
  .brand-tagline {
    font-size: 15.5px; color: var(--text-grey); letter-spacing: 1.1px;
    margin-top: 6px;
  }

  /* front: info bands */
  .band { position: absolute; top: 191px; height: 113px; color: var(--white); }
  .band-person {
    left: 0; width: 294px; background: var(--leaf-green);
    text-align: right; padding: 14px 24px 0 0;
  }
  .band-contact {
    left: 299px; width: 301px; background: var(--ocean-blue);
    padding: 16px 0 0 22px;
  }
  .person-name { font-size: 23px; font-weight: 500; line-height: 1.05; }
  .person-title { font-size: 15px; line-height: 1.3; }
  .person-address { font-size: 13.5px; line-height: 1.4; margin-top: 2px; }
  .contact-list { list-style: none; }
  .contact-list li {
    display: flex; align-items: center; gap: 8px;
    font-size: 14px; line-height: 19.5px;
  }
  .contact-list svg { width: 13px; height: 13px; flex: none; fill: var(--white); }

  /* back */
  .back-emblem {
    position: absolute; left: 226px; top: 68px;
    width: 148px; height: 148px; border-radius: 50%;
    border: 2px solid var(--lime);
    padding: 5px;
  }
  .back-emblem span {
    display: block; width: 100%; height: 100%; border-radius: 50%;
    background: var(--lime);
  }
  .back-name {
    position: absolute; left: 0; right: 0; top: 226px;
    text-align: center; font-size: 33px; font-weight: 600;
    color: var(--lime); letter-spacing: -0.3px; line-height: 1.1;
  }
</style>
</head>
<body>

<section class="card card-front">
  <div class="brand">
    <span class="brand-dot"></span>
    <div>
      <div class="brand-name">KeenTraders.example</div>
      <div class="brand-tagline">Outings-Eateries-Wellness-Style</div>
    </div>
  </div>

  <div class="band band-person">
    <div class="person-name">ELLIS MORAN</div>
    <div class="person-title">CEO/FOUNDER</div>
    <div class="person-address">48730 West 61st Avenue<br>Suite C204, Phoenix AZ 85917</div>
  </div>

  <div class="band band-contact">
    <ul class="contact-list">
      <li><svg viewBox="0 0 16 16"><path d="M3.6 1.2l2.2 2.6c.4.5.3 1.1-.1 1.5L4.6 6.3c.9 2 2.5 3.6 4.5 4.6l1-1.1c.4-.4 1-.5 1.5-.1l2.6 2.2c.5.4.5 1.1.1 1.6l-1.2 1.3c-.5.5-1.3.7-2 .4C6.2 13.5 2.6 9.9.9 5.1.6 4.4.8 3.6 1.3 3.1L2.6 1.8c.3-.5.7-.6 1-.6z"/></svg>555 014 2638</li>
      <li><svg viewBox="0 0 16 16"><path d="M4.5 0h7A1.5 1.5 0 0 1 13 1.5v13a1.5 1.5 0 0 1-1.5 1.5h-7A1.5 1.5 0 0 1 3 14.5v-13A1.5 1.5 0 0 1 4.5 0zM5 2v10h6V2zm3 11a1 1 0 1 0 0 2 1 1 0 0 0 0-2z"/></svg>555 019 7441</li>
      <li><svg viewBox="0 0 16 16"><path d="M1 3h14v10H1zm1.5 1.2v.3L8 8.6l5.5-4.1v-.3zm0 2.1v5.2h11V6.3L8 10.4z"/></svg>ellis@keentraders.example</li>
      <li><svg viewBox="0 0 16 16"><path d="M8 0a8 8 0 1 0 0 16A8 8 0 0 0 8 0zm-1 2.2c-.6.8-1.6 1.3-1.4 2.4.2 1 1.6.7 2 1.6.4.9-.6 1.6-.2 2.6.4 1 1.7.8 1.8 2 .1 1.1-.7 2-1.2 2.9A6 6 0 0 1 7 2.2zm3.3.6a6 6 0 0 1 3.4 6.4c-.7-.3-1.2-1-2-1-.9 0-1.2-1-.8-1.8.4-.9 1.3-1.5.6-2.6-.3-.4-.8-.6-1.2-1z"/></svg>www.keentraders.example</li>
    </ul>
  </div>
</section>

<section class="card card-back">
  <div class="back-emblem"><span></span></div>
  <div class="back-name">Bright Harbor Ventures</div>
</section>

</body>
</html>
```